Magnetic Business card Design do a service provider

Hi,

The company aim is to provide all service needs under one roof. However, at the moment there is only Accounting, Electrical and IT branches. There will be more services coming onboard in the future.

I already have a logo designed (Company name is already part of the logo), I now need a magnetic business card designed.

The business card will contain the following:

- Company Logo
- Contact#
- E-mail
- enough space to add website URL (for future)
Updates

Project Deadline Extended Reason: HI All,The deadline has been extended due to not having enough time to review an overwhelming number of designs that has been submitted by lots of designers.I will be uploading a draft of designs that i have in mind.Thanks. Added Friday, January 22, 2016

Target Market(s)

Residential, Home-based Businesses, Small and Medium businesses

Industry/Entity Type

Business

Contact Information for Business Card

Contact#: 0491 738 520
E-mail: service@brightlanetrades.net.au

Font styles to use
Decorative
Script

Requirements
Must have
• Round edges
• Some form of logo incorporation as a background

```html
<!DOCTYPE html>
<html lang="en">
<head>
<meta charset="utf-8">
<title>Bright Lane Trades – Business Card</title>
<link href="https://fonts.googleapis.com/css2?family=Open+Sans:wght@400;600&display=swap" rel="stylesheet">
<style>
  :root {
    --backdrop: #4a4039;
    --card: #1c1d1f;
    --card-edge: #111213;
    --brand-blue: #1f6fb8;
    --text-light: #e9e9ea;
    --text-muted: #b9bbbe;
    --divider: #8d9094;
  }
  * { box-sizing: border-box; margin: 0; padding: 0; }
  html, body {
    width: 1200px;
    height: 787px;
    overflow: hidden;
    background: var(--backdrop);
    font-family: "Open Sans", Arial, sans-serif;
  }
  .canvas {
    position: relative;
    width: 1200px;
    height: 787px;
    display: flex;
    align-items: center;
    justify-content: center;
    gap: 60px;
  }
  .card {
    position: relative;
    width: 520px;
    height: 300px;
    background: var(--card);
    border-radius: 14px;
    box-shadow: 0 0 0 1px var(--card-edge);
    overflow: hidden;
  }

  /* Brand lockup: invented name as plain text with one circle */
  .brand {
    position: absolute;
    display: flex;
    align-items: center;
    gap: 10px;
    color: var(--brand-blue);
    font-weight: 600;
    white-space: nowrap;
  }
  .brand__dot {
    width: 22px;
    height: 22px;
    border-radius: 50%;
    background: var(--brand-blue);
    flex: none;
  }

  /* Front */
  .card--front .brand {
    left: 50%;
    top: 108px;
    transform: translateX(-50%);
    font-size: 30px;
  }
  .card--front .brand .brand__dot { width: 26px; height: 26px; }
  .front__url {
    position: absolute;
    left: 0;
    right: 0;
    top: 196px;
    text-align: center;
    color: var(--text-light);
    font-size: 19px;
    letter-spacing: 2px;
  }

  /* Back */
  .card--back .brand {
    left: 50%;
    top: 78px;
    transform: translateX(-38%);
    font-size: 25px;
  }
  .holder {
    position: absolute;
    left: 40px;
    top: 176px;
    width: 120px;
    text-align: right;
  }
  .holder__name {
    color: var(--brand-blue);
    font-size: 17px;
    font-weight: 600;
  }
  .holder__role {
    color: var(--text-light);
    font-size: 14px;
    margin-top: 2px;
  }
  .divider {
    position: absolute;
    left: 178px;
    top: 168px;
    width: 1px;
    height: 78px;
    background: var(--divider);
  }
  .contacts {
    position: absolute;
    left: 196px;
    top: 168px;
    list-style: none;
  }
  .contacts__item {
    display: flex;
    align-items: center;
    gap: 10px;
    height: 26px;
    color: var(--text-light);
    font-size: 14px;
  }
  .contacts__icon { width: 14px; height: 14px; flex: none; }
</style>
</head>
<body>
<main class="canvas">

  <section class="card card--front" aria-label="Card front">
    <div class="brand">
      <span class="brand__dot"></span>
      <span class="brand__name">Bright Lane Trades</span>
    </div>
    <p class="front__url">brightlanetrades.net.au</p>
  </section>

  <section class="card card--back" aria-label="Card back">
    <div class="brand">
      <span class="brand__dot"></span>
      <span class="brand__name">Bright Lane Trades</span>
    </div>

    <div class="holder">
      <p class="holder__name">Sam Porter</p>
      <p class="holder__role">President</p>
    </div>

    <span class="divider"></span>

    <ul class="contacts">
      <li class="contacts__item">
        <svg class="contacts__icon" viewBox="0 0 24 24" aria-hidden="true">
          <path fill="#1f6fb8" d="M6.6 10.8a15.1 15.1 0 0 0 6.6 6.6l2.2-2.2c.3-.3.7-.4 1-.2 1.1.4 2.3.6 3.6.6.6 0 1 .4 1 1V20c0 .6-.4 1-1 1C10.6 21 3 13.4 3 4c0-.6.4-1 1-1h3.5c.6 0 1 .4 1 1 0 1.3.2 2.5.6 3.6.1.3 0 .7-.2 1z"/>
        </svg>
        <span>0491 738 520</span>
      </li>
      <li class="contacts__item">
        <svg class="contacts__icon" viewBox="0 0 24 24" aria-hidden="true">
          <rect x="2" y="5" width="20" height="14" rx="2" fill="#1f6fb8"/>
          <path d="M3 6l9 7 9-7" fill="none" stroke="#1c1d1f" stroke-width="2"/>
        </svg>
        <span>service@brightlanetrades.net.au</span>
      </li>
      <li class="contacts__item">
        <svg class="contacts__icon" viewBox="0 0 24 24" aria-hidden="true">
          <circle cx="12" cy="12" r="10" fill="#1f6fb8"/>
          <path d="M2 12h20M12 2c3 3 3 17 0 20M12 2c-3 3-3 17 0 20" fill="none" stroke="#1c1d1f" stroke-width="1.5"/>
        </svg>
        <span>www.brightlanetrades.net.au</span>
      </li>
    </ul>
  </section>

</main>
</body>
</html>
```